PLUMBING VAN LOGO/VINYL GRAPHIC CONTEST!

Our target audience is builders, contractors, designers, architects.

Upon discussion with some vinyl wrap companies we are now moving away from a full wrap and going for more simplistic lettering and logo design on the truck.
We are looking to apply vinyl graphics on top of a silver color Brannoc hauler 3400. (See attached picture for JUST CUT VINYL style design.

We would like to have our logo incorporated on to the sides of the truck (Must be shrunken down to fit the full logo - no cut off half images)

We would also like to have Custom homes, Additions, Renovations, as well as Commercial/Industrial incorporated onto the side of the van and also the back doors.

We would like to see variations of black and blue on top of the silver for a good color contrast. No light colours for the writing.

Hi Designers,

We are going to be changing the overall design stance of our project, we didn't find anything we particularly liked enough to use as a wrap for our trucks.

We would like to see some more simplistic ideas, and we have decided to keep the silver color of our trucks as a background. We will be going with vinyl graphics on top of the silver backdrop, instead of a full van wrap/color change.

With any new submissions, we would prefer to see our logo and our services listed on the truck, with different ideas for placement. Having a silver van color, we would prefer some darker bolder colors like black, blue, etc. and to avoid any light color schemes.

Important things to have on the design

Kestrow Plumbing Ltd
(logo)
(custom homes, additions, renovations)
(commercial/industrial)

Thank you to everybody who has/will submit designs.

• We are open to different fonts. We like the font in the logo but are open to other ideas.

• Kestrow Plumbing Ltd , Custom Homes, Additions, Renovations, Commercial/Residential
• Silver background on van, kestrow plumbing logo and kestrow plumbing ltd written on

```html
<!DOCTYPE html>
<html lang="en">
<head>
<meta charset="utf-8">
<title>Kestrow Plumbing – Van Side Vinyl Graphics</title>
<link rel="stylesheet" href="https://fonts.googleapis.com/css2?family=Montserrat:wght@300;500;600;700&display=swap">
<style>
  :root {
    --silver: #9c9d9f;
    --brand-blue: #0a5ec0;
    --ink: #111111;
    --white: #ffffff;
  }
  html, body {
    margin: 0;
    padding: 0;
    overflow: hidden;
  }
  body {
    width: 1200px;
    height: 1200px;
    background: var(--silver);
    font-family: "Montserrat", sans-serif;
  }
  .van-side {
    position: relative;
    width: 1200px;
    height: 1200px;
  }
  .contact {
    position: absolute;
    left: 122px;
    top: 604px;
    display: flex;
    align-items: center;
    gap: 10px;
  }
  .social-dots {
    display: flex;
    gap: 9px;
  }
  .social-dot {
    width: 22px;
    height: 22px;
    border-radius: 50%;
    background: var(--brand-blue);
  }
  .phone {
    margin-left: 14px;
    font-weight: 600;
    font-size: 22px;
    line-height: 30px;
    color: var(--ink);
    letter-spacing: 0.5px;
    white-space: nowrap;
  }
  .brand-mark {
    position: absolute;
    left: 480px;
    top: 440px;
    width: 120px;
    height: 120px;
    box-sizing: border-box;
    border: 3px solid var(--brand-blue);
  }
  .brand-name {
    position: absolute;
    left: 420px;
    top: 614px;
    width: 240px;
    text-align: center;
    color: var(--brand-blue);
    font-weight: 500;
    line-height: 1;
    white-space: nowrap;
  }
  .brand-name .word-main {
    display: block;
    font-size: 33px;
    letter-spacing: 1px;
  }
  .brand-name .word-sub {
    display: block;
    margin-top: 6px;
    font-size: 15px;
    letter-spacing: 6px;
  }
  .sector-line {
    position: absolute;
    left: 698px;
    top: 402px;
    margin: 0;
    font-weight: 300;
    font-size: 22px;
    letter-spacing: 4.5px;
    color: var(--white);
    white-space: nowrap;
  }
  .services {
    position: absolute;
    left: 650px;
    top: 484px;
    width: 500px;
    margin: 0;
    text-align: center;
    font-weight: 700;
    font-size: 24px;
    line-height: 1.2;
    color: var(--brand-blue);
    white-space: nowrap;
  }
  .services .divider {
    font-weight: 500;
  }
  .website {
    position: absolute;
    left: 650px;
    top: 590px;
    width: 500px;
    margin: 0;
    text-align: center;
    font-weight: 600;
    font-size: 21px;
    color: var(--ink);
    white-space: nowrap;
  }
  .rear-stripe {
    position: absolute;
    left: 1020px;
    top: 525px;
  }
</style>
</head>
<body>
  <main class="van-side">
    <div class="contact">
      <div class="social-dots">
        <span class="social-dot"></span>
        <span class="social-dot"></span>
        <span class="social-dot"></span>
      </div>
      <span class="phone">(555) 014-2290</span>
    </div>

    <div class="brand-mark"></div>
    <div class="brand-name">
      <span class="word-main">KESTROW</span>
      <span class="word-sub">PLUMBING</span>
    </div>

    <p class="sector-line">COMMERCIAL / INDUSTRIAL</p>

    <p class="services">COSTUM HOMES <span class="divider">|</span> ADDITIONS<br>RENOVATIONS</p>

    <p class="website">www.kestrowplumbing.com</p>

    <svg class="rear-stripe" width="150" height="215" viewBox="0 0 150 215">
      <polygon points="150,0 150,80 60,215 5,215" fill="var(--brand-blue)"/>
      <polygon points="150,120 150,215 95,215" fill="var(--brand-blue)"/>
    </svg>
  </main>
</body>
</html>
```